Brightvale Wound Care
Business cards and letterhead
Professional
Gregory Tamsett
Chief Executive Officer
3470 P Street NW
Suite 615
Washington, DC 20011
gtamsett@brightvale-wc.example
www.brightvale-wc.example
I need one that says "CEO" for the name above and one that says "Territory Manager". I also need (with the same design for the name Darren Pulcombe as "President" and one for him as well that says Senior Territory Manager"
I need to list these products on the back:
1. Verashu Negitive Pressure Wound Therapy
2. Brunix Negitive Pressure Wound Therapy
3. Orvil alternating pressure mattresses
Here is our logo please use this logo while doing our design for this project for both the business cards and letterhead. Thanks
Please add this one or the non-green one (also uploaded) some where on the card. Make it very small please.
Or add this one to the card somewhere. Whatever one looks better.

```html
<!DOCTYPE html>
<html lang="en">
<head>
<meta charset="utf-8">
<title>Brightvale Wound Care – Stationery</title>
<link rel="stylesheet" href="https://fonts.googleapis.com/css2?family=Jost:wght@400;500;600&display=swap">
<style>
  :root {
    --brand-blue: #2b3f9c;
    --brand-blue-dark: #1f2f7e;
    --brand-red: #c8203a;
    --ink: #3a3f55;
    --paper: #ffffff;
    --frame: #d6d6d6;
    --stage: #ffffff;
  }
  * { box-sizing: border-box; margin: 0; padding: 0; }
  html, body { width: 1200px; height: 921px; overflow: hidden; background: var(--stage); }
  body { font-family: "Jost", "Futura", sans-serif; color: var(--ink); }

  .stage {
    position: relative;
    width: 1200px; height: 921px;
    border: 2px solid var(--frame);
  }

  /* Letterhead */
  .letterhead {
    position: absolute;
    left: 95px; top: 62px;
    width: 595px; height: 780px;
    background: var(--paper);
    box-shadow: 0 1px 4px rgba(0,0,0,.25);
    overflow: hidden;
  }
  .letterhead .band { position: absolute; left: 0; top: 0; width: 100%; height: 120px; }
  .letterhead .wordmark {
    position: absolute; right: 40px; top: 112px;
    display: flex; align-items: center; gap: 8px;
    font-size: 22px; font-weight: 500; color: var(--brand-blue);
  }
  .wordmark .dot { width: 14px; height: 14px; border-radius: 50%; background: var(--brand-red); }
  .letterhead .footer {
    position: absolute; left: 40px; bottom: 32px;
    font-size: 11px; line-height: 1.45; color: var(--brand-blue); font-weight: 500;
  }

  /* Cards */
  .cards {
    position: absolute; left: 740px; top: 62px;
    display: flex; flex-direction: column; gap: 17px;
  }
  .card {
    position: relative;
    width: 285px; height: 143px;
    background: var(--paper);
    box-shadow: 0 1px 4px rgba(0,0,0,.25);
    overflow: hidden;
  }
  .card .band { position: absolute; left: 0; top: 0; width: 100%; height: 60px; }
  .card .base { position: absolute; left: 0; bottom: 0; width: 100%; height: 9px; background: var(--brand-blue); }
  .card .wordmark {
    position: absolute; right: 14px; top: 40px;
    display: flex; align-items: center; gap: 4px;
    font-size: 10.5px; font-weight: 500; color: var(--brand-blue);
  }
  .card .wordmark .dot { width: 7px; height: 7px; }
  .card .person { position: absolute; left: 16px; top: 58px; }
  .person .name { font-size: 10px; font-weight: 600; color: var(--brand-red); }
  .person .title { font-size: 7.5px; color: var(--brand-blue); margin-top: 1px; }
  .card .contact {
    position: absolute; left: 16px; top: 94px;
    font-size: 5.6px; line-height: 1.5; color: var(--ink);
  }

  .card.back { background: var(--brand-blue); }
  .card.back .mark-zone {
    position: absolute; left: 28px; top: 24px;
    width: 92px; height: 92px; border-radius: 50%;
    background: rgba(255,255,255,.12);
  }
  .card.back .products {
    position: absolute; left: 128px; top: 50px;
    list-style: none; font-size: 6.4px; line-height: 2; color: #fff;
  }
  .products li::before { content: "•"; color: #fff; margin-right: 5px; }
</style>
</head>
<body>
<div class="stage">

  <section class="letterhead">
    <svg class="band" viewBox="0 0 595 120" preserveAspectRatio="none" aria-hidden="true">
      <path d="M0 0 H595 V40 C430 18 220 36 0 82 Z" fill="var(--brand-blue)"/>
      <path d="M0 92 C220 46 430 28 595 50" fill="none" stroke="var(--brand-red)" stroke-width="3.5"/>
      <path d="M0 99 C220 54 430 36 595 58" fill="none" stroke="var(--brand-blue)" stroke-width="1.5" opacity=".5"/>
    </svg>
    <div class="wordmark"><span class="dot"></span>Brightvale Wound Care</div>
    <address class="footer" style="font-style:normal">
      3470 P Street NW, Suite 615, Washington, DC 20011<br>
      Phone: 202-555-0148 | Fax: 202-555-0193 | www.brightvale-wc.example
    </address>
  </section>

  <div class="cards">
    <article class="card">
      <svg class="band" viewBox="0 0 285 60" preserveAspectRatio="none" aria-hidden="true">
        <path d="M0 0 H285 V20 C200 8 100 16 0 38 Z" fill="var(--brand-blue)"/>
        <path d="M0 44 C100 22 200 14 285 26" fill="none" stroke="var(--brand-red)" stroke-width="2"/>
      </svg>
      <div class="wordmark"><span class="dot"></span>Brightvale Wound Care</div>
      <div class="person"><p class="name">Gregory Tamsett</p><p class="title">Chief Executive Officer</p></div>
      <p class="contact">3470 P Street NW, Suite 615, Washington, DC 20011<br>Phone: 202-555-0148 | Fax: 202-555-0193<br>Email: gtamsett@brightvale-wc.example | www.brightvale-wc.example</p>
      <div class="base"></div>
    </article>

    <article class="card">
      <svg class="band" viewBox="0 0 285 60" preserveAspectRatio="none" aria-hidden="true">
        <path d="M0 0 H285 V20 C200 8 100 16 0 38 Z" fill="var(--brand-blue)"/>
        <path d="M0 44 C100 22 200 14 285 26" fill="none" stroke="var(--brand-red)" stroke-width="2"/>
      </svg>
      <div class="wordmark"><span class="dot"></span>Brightvale Wound Care</div>
      <div class="person"><p class="name">Gregory Tamsett</p><p class="title">Territory Manager</p></div>
      <p class="contact">3470 P Street NW, Suite 615, Washington, DC 20011<br>Phone: 202-555-0148 | Fax: 202-555-0193<br>Email: gtamsett@brightvale-wc.example | www.brightvale-wc.example</p>
      <div class="base"></div>
    </article>

    <article class="card">
      <svg class="band" viewBox="0 0 285 60" preserveAspectRatio="none" aria-hidden="true">
        <path d="M0 0 H285 V20 C200 8 100 16 0 38 Z" fill="var(--brand-blue)"/>
        <path d="M0 44 C100 22 200 14 285 26" fill="none" stroke="var(--brand-red)" stroke-width="2"/>
      </svg>
      <div class="wordmark"><span class="dot"></span>Brightvale Wound Care</div>
      <div class="person"><p class="name">Darren Pulcombe</p><p class="title">President</p></div>
      <p class="contact">3470 P Street NW, Suite 615, Washington, DC 20011<br>Phone: 202-555-0148 | Fax: 202-555-0193<br>Email: dpulcombe@brightvale-wc.example | www.brightvale-wc.example</p>
      <div class="base"></div>
    </article>

    <article class="card">
      <svg class="band" viewBox="0 0 285 60" preserveAspectRatio="none" aria-hidden="true">
        <path d="M0 0 H285 V20 C200 8 100 16 0 38 Z" fill="var(--brand-blue)"/>
        <path d="M0 44 C100 22 200 14 285 26" fill="none" stroke="var(--brand-red)" stroke-width="2"/>
      </svg>
      <div class="wordmark"><span class="dot"></span>Brightvale Wound Care</div>
      <div class="person"><p class="name">Darren Pulcombe</p><p class="title">Territory Manager</p></div>
      <p class="contact">3470 P Street NW, Suite 615, Washington, DC 20011<br>Phone: 202-555-0148 | Fax: 202-555-0193<br>Email: dpulcombe@brightvale-wc.example | www.brightvale-wc.example</p>
      <div class="base"></div>
    </article>

    <article class="card back">
      <div class="mark-zone" role="img" aria-label="Faint brand mark area"></div>
      <ul class="products">
        <li>Verashu Negative Pressure Wound Therapy</li>
        <li>Brunix Negative Pressure Wound Therapy</li>
        <li>Orvil alternating pressure mattresses</li>
      </ul>
    </article>
  </div>

</div>
</body>
</html>
```